Ecommerce brand for entrepreneurs needs help with branding products

I am looking for help to design a small supplement pouch. Including colours, layout and design.

The business:
The business is called 'Tall Ember' and our goal is to help entrepreneurs continue to change the world in spite of how difficult it is.

At Tall Ember, we understand being an entrepreneur is one of the hardest jobs there is. We believe there is a better way. A way in which you don’t have to choose between success in your business and the rest of your life. Our aim is to solve these challenges, so you can stay in the fight a little longer. If we can do this, we can ultimately change the world into a better place.

We will do this through a range of supplements, community, information and physical products to help you optimise their lives.

The product:
The product I am looking to create is for a natural nootropic called

‘The Quiet Lantern’

The product will address the challenges with focus and lower attention spans.

So Entrepreneurs can Solve more problems, Help more people and make more money.

Do more in four hours than a whole day. Have Zen like calm. With Zero Jitters & Zero Crashes. Do what others can’t

The design:
I want this to be a small pouch. The final design should be elegant, and minimalist and have an edge that is different.

I have added examples of products that I like below.

I am open to most colour combinations but silver, navy, black, orange, white and translucent are what is taking my fancy right now.

I like the idea of having a translucent package or part of the package like some of the designs below. I also like the matt finish of some of the designs along with the flashes of shininess from silver for contrast. or even using embossing within the packaging.

I have a logo that I have made but I am open to changes on that as well if you see fit. if you do want to do this, I would love to see an emblem next to the words Tall Ember that encapsulates the brand.

I have done some really really rough mockups myself but would like to see what you have to offer rather than what I have done

The purpose of this image:
I need a 3D mockup of this supplement to be on my landing page to start to take pre-orders.

I am ideally looking for 2 images

1) Supplement packaging on its own
2) Supplement packaging with background coloured lighting, with powder on the ground etc

Need extra days to review

The logo: Please also redesign my logo - I would love to see an emblem next to the words Tall Ember that encapsulates the brand.The business is called 'Tall Ember' and our goal is to help entrepreneurs continue to change the world in spite of how difficult it is. At Tall Ember, we understand being an entrepreneur is one of the hardest jobs there is. We believe there is a better way. A way in which you don’t have to choose between success in your business and the rest of your life. Our aim is to solve these challenges, so you can stay in the fight a little longer. If we can do this, we can ultimately change the world into a better place. We will do this through a range of supplements, community, information and physical products to help you optimise their lives.

Supplements for entrepreneurs

• The design: I want this to be a small pouch. The final design should be elegant, and minimalist and have an edge that is different. I have added examples of products that I like below. I am open to most colour combinations but silver, navy, black, orange, white and translucent are what is taking my fancy right now. I like the idea of having a translucent package or part of the package like some of the designs below. I also like the matt finish of some of the designs along with the flashes of shininess from silver for contrast. or even using embossing within the packaging.

```html
<!DOCTYPE html>
<html lang="en">
<head>
<meta charset="utf-8">
<title>Tall Ember – The Quiet Lantern</title>
<link href="https://fonts.googleapis.com/css2?family=Russo+One&family=Montserrat:wght@700&family=Arimo:wght@400;700&display=swap" rel="stylesheet">
<style>
  :root {
    --stage: #0050ff;
    --pouch-light: #1250d0;
    --pouch-mid: #0a3aa8;
    --pouch-dark: #021a4c;
    --accent: #3b9fd0;
    --brand: #2b8dbb;
    --silver: #e4e2de;
    --copy: #d6d8e2;
    --dots-a: #0a3cb0;
    --dots-b: #06287a;
  }
  * { margin: 0; padding: 0; box-sizing: border-box; }
  html, body {
    width: 1195px; height: 1200px; overflow: hidden;
    background: var(--stage);
  }
  .canvas { position: relative; width: 1195px; height: 1200px; }
  .pouch {
    position: absolute; left: 245px; top: 71px; width: 680px; height: 990px;
    border-radius: 22px; overflow: hidden;
    background: linear-gradient(100deg, var(--pouch-light) 0%, var(--pouch-mid) 42%, var(--pouch-dark) 75%);
  }
  .pouch > * { position: absolute; }
  .count, .category {
    font-family: "Arimo", Arial, sans-serif; font-size: 24px; color: var(--accent); top: 48px;
  }
  .count { left: 49px; top: 52px; }
  .category { right: 62px; }
  .product-name {
    left: 0; right: 0; top: 266px; text-align: center;
    font-family: "Russo One", sans-serif; font-size: 46px; color: var(--silver);
    font-variant: small-caps; letter-spacing: 1px;
  }
  .brand {
    left: 323px; top: 440px;
    font-family: "Montserrat", sans-serif; font-weight: 700; color: var(--brand);
    font-size: 58px; line-height: 78px; letter-spacing: 10px;
  }
  .brand-row { display: flex; align-items: center; gap: 18px; }
  .brand-mark { width: 40px; height: 40px; background: var(--brand); }
  .formula {
    left: 49px; top: 664px;
    font-family: "Arimo", Arial, sans-serif; font-weight: 700; font-size: 31px; color: var(--accent);
  }
  .tagline {
    left: 49px; top: 702px; width: 480px;
    font-family: "Arimo", Arial, sans-serif; font-size: 23px; line-height: 30px; color: var(--copy);
  }
  .texture { left: 0; bottom: 0; width: 680px; height: 260px; }
</style>
</head>
<body>
<main class="canvas">
  <section class="pouch">
    <p class="count">60 CAPSULES</p>
    <p class="category">Food Supplement</p>
    <h1 class="product-name">The Quiet Lantern</h1>
    <div class="brand">
      <div class="brand-row"><span>TALL</span><span class="brand-mark"></span></div>
      <div>EMBER.</div>
    </div>
    <h2 class="formula">DAILY MULTY COMPLEX</h2>
    <p class="tagline">Essential vitamins and minerals to support your lifestyle and fill nutrient gaps.</p>
    <svg class="texture" viewBox="0 0 680 260" role="img" aria-label="Decorative halftone dot wave pattern">
      <defs>
        <linearGradient id="wave" x1="0" y1="1" x2="1" y2="0">
          <stop offset="0" stop-color="var(--dots-b)"/>
          <stop offset="1" stop-color="var(--dots-a)"/>
        </linearGradient>
      </defs>
      <path d="M0 150 C160 120 300 110 420 90 C540 70 620 30 680 0 L680 260 L0 260 Z" fill="url(#wave)" opacity="0.85"/>
    </svg>
  </section>
</main>
</body>
</html>
```